Innovative Webpage for leadership development and training company

Bright Harbour is a company supporting small organisations, in particular NGOs or projects, to increase the impact of their training and to increase the retention of talent through customized leadership development solutions. We help organisations to Guide Well & Coach Well
We want to have a simple but modern design webpage that stands outs from the usual consulting webpages
Here you are two possible examples of consulting firms approaching the same target audience
http://www.quillmarsh.eu/
http://borvencast.com/#intro
The webpage should be designed and developed in a platform that allows full customization in the future both in terms of pages, text and images
It should allow the integration of two short videos that are currently under development
It should allow the maximum possible interoperabililty with tables and smartphones

Target Market(s)

Nonprofit, young professionals, technical assistance and capacity building projects, global SMEs, multicultural teals

Industry/Entity Type

Leadership

Number of Pages Required

5+ page

Requirements
Must have
• A dynamic/engaging/modern homepage
• A design that can be easily transferable to other pages
• A user-friendly platform that allows complete customization
• Evaluation Criteria
• 1. Overall Design/Feel of the webpage (in particular homepage). Our company looks for innovative leadership development and training. We often step out of our comfort zone in a playful positive way and that requires courage.
• 2. Flexibility to edit and/or translate homepage design to new/other pages
• 3. User-friendliness to customize, change the webpage
• 4. Completeness of coded pages (# of pages effectively developed)
Nice to have
• The maximum number of coded pages designed as per the attached file

```html
<!DOCTYPE html>
<html lang="en">
<head>
<meta charset="utf-8">
<title>Bright Harbour — Consulting · Training · Coaching</title>
<link href="https://fonts.googleapis.com/css2?family=Open+Sans:ital,wght@0,400;0,600;0,700;0,800;1,400&display=swap" rel="stylesheet">
<style>
:root{
  --orange:#f39200;
  --orange-deep:#e8760a;
  --blue:#2a5fa3;
  --blue-dark:#1d4a86;
  --navy:#2d3e56;
  --ink:#333;
  --white:#fff;
}
*{margin:0;padding:0;box-sizing:border-box}
html,body{width:1200px;height:4642px;overflow:hidden}
body{font-family:"Open Sans",Arial,sans-serif;color:var(--ink);background:var(--white);font-size:13px;line-height:1.5}
section,header,footer{position:relative;width:1200px;overflow:hidden}

/* hero */
.hero{height:687px;background:linear-gradient(180deg,#2b2b2b 0%,#5a5a5a 45%,#3a3a3a 100%);text-align:center;color:var(--white)}
.hero-photo{position:absolute;inset:0;background:radial-gradient(ellipse at 60% 70%,rgba(150,150,150,.45),rgba(20,20,20,0) 60%)}
.brand{position:absolute;top:150px;left:0;right:0}
.brand-name{font-size:60px;font-weight:700;letter-spacing:1px;display:inline-flex;align-items:center;gap:18px}
.brand-dot{width:38px;height:38px;border-radius:50%;background:var(--orange)}
.brand-tag{font-size:20px;margin-top:2px;letter-spacing:1px}
.hero-title{position:absolute;top:478px;left:0;right:0;font-size:70px;font-weight:600;color:var(--orange);letter-spacing:-1px}
.hero-chevron{position:absolute;top:600px;left:570px}

/* nav */
.nav{height:50px;background:var(--orange);display:flex;justify-content:space-between;align-items:center;padding:0 125px}
.nav a{color:var(--white);text-decoration:none;font-size:14px;font-weight:700;text-transform:uppercase;letter-spacing:1px}

/* about */
.about{height:687px;background:linear-gradient(180deg,#fafafa,#e9e9e9);text-align:center;padding:36px 190px 0}
.section-title{font-size:44px;font-weight:700;letter-spacing:6px;text-transform:uppercase}
.rule{width:300px;height:2px;background:#333;margin:10px auto 24px}
.about p{font-size:12.5px;margin-bottom:10px}
.about h3{color:var(--blue);font-size:21px;font-weight:600;margin:26px 0 4px}
.about .lead{color:var(--orange);font-weight:600}

/* team */
.team{height:486px;background:linear-gradient(180deg,#c88a2a 0%,#d7901c 40%,#b8761a 100%);color:var(--white);text-align:center;padding:40px 190px 0}
.team-title{font-size:34px;font-weight:600}
.team .rule{background:var(--white);width:280px;margin:8px auto 26px}
.team h4{font-size:22px;font-weight:600;margin-bottom:6px}
.team p{font-size:12.5px;margin-bottom:26px}

/* services */
.services{height:938px;background:linear-gradient(160deg,var(--blue) 0%,var(--blue-dark) 100%);color:var(--white);padding:34px 185px 0}
.services .section-title,.clients .section-title{text-align:center;color:var(--white);font-size:38px;font-weight:600}
.services .rule,.clients .rule{background:var(--white);width:460px;margin:8px auto 22px}
.services h2{font-size:28px;font-weight:600;margin-bottom:8px}
.services h5{font-size:14px;font-weight:700;margin:9px 0 2px}
.services p{font-size:11.5px;margin-bottom:3px;line-height:1.4}
.services ul{font-size:11.5px;padding-left:34px;line-height:1.4}

/* clients */
.clients{height:1139px;background:linear-gradient(180deg,var(--orange) 0%,var(--orange-deep) 100%);color:var(--white);padding:62px 185px 0}
.clients h5{font-size:14px;font-weight:700;margin:22px 0 6px}
.clients p{font-size:12.5px}
.testimonial{position:absolute;top:655px;left:0;width:1200px;height:300px}
.client-photo{position:absolute;left:190px;top:10px;width:270px;height:270px;border-radius:50%;border:6px solid var(--white);background:radial-gradient(circle at 50% 40%,#c9b8a6,#5f6f7e)}
.client-role{position:absolute;left:620px;top:10px;width:420px;font-size:15px}
.client-quote{position:absolute;left:620px;top:80px;width:420px;font-size:21px;font-style:italic;line-height:1.25;color:#fde6c5}
.next-arrow{position:absolute;left:1058px;top:120px}

/* footer */
.footer{height:655px;display:flex}
.map{width:720px;height:655px;background:linear-gradient(135deg,#e8e6e1,#d9dcd6 60%,#ececec)}
.contact{flex:1;background:var(--navy);color:var(--white);position:relative}
.contact-mail{position:absolute;top:108px;left:40px;font-size:26px}
.social{position:absolute;top:480px;left:150px;display:flex;gap:14px}
.social span{width:48px;height:48px;background:var(--white);display:block}
</style>
</head>
<body>

<header class="hero">
  <div class="hero-photo" role="img" aria-label="Dark photo of runners on a track"></div>
  <div class="brand">
    <div class="brand-name"><span class="brand-dot"></span>Bright Harbour</div>
    <div class="brand-tag">Consulting - Training - Coaching</div>
  </div>
  <h1 class="hero-title">Guide Well. Coach Well</h1>
  <svg class="hero-chevron" width="60" height="50" viewBox="0 0 60 50" fill="none" stroke="#f39200" stroke-width="5"><path d="M8 6 L30 24 L52 6"/><path d="M8 24 L30 42 L52 24"/></svg>
</header>

<nav class="nav">
  <a href="#">Home</a><a href="#">About</a><a href="#">Team</a><a href="#">Service</a><a href="#">Portfolio</a><a href="#">Contact</a>
</nav>

<section class="about">
  <h2 class="section-title">About Us</h2>
  <div class="rule"></div>
  <p>Bright Harbour SPRL offers tailor-made innovative solutions for organisational and individual excellence. We strive to increase the capacity and impact of non-profit organisations, international development and public-private projects and SMEs through customised services in leadership development, executive coaching and training.</p>
  <h3>Mission Statement</h3>
  <p>We share innovation, inspiration and collaboration with partners to support their learning and development capacity and increase the impact of their projects and initiatives.</p>
  <h3>Our Core Benefits for Global Organisations</h3>
  <p><span class="lead">Context:</span> Understanding and being able to respond to changes in the external environment. The pace of change, technologically, politically and socially is continuously increasing, leaving individuals permanently with the need to learn and to adapt in a constantly new and changing environment and set of relationships. More often than not we need ‘ad hoc’ and contextual solutions that require a more complex decision making process.</p>
  <p><span class="lead">Complexity:</span> Having the skills to survive and thrive in situations of low certainty and low agreement. The diversity of social rules and conventions in international environments that we are exposed to makes it increasingly difficult to find ‘the right way’ of doing tasks in our private and professional lives.</p>
  <p><span class="lead">Connectedness:</span> The uncertain economic environment and the interdependence of the economic actors makes increasingly difficult for leaders and organisations, and individuals in general, to anticipate the immediate future. The ability to communicate, to create resilient relationships and teams that can absorb and create change is more and more pressing, and there are neither simple solutions nor magic recipes, just the willingness to explore and be confronted with the uncertainty.</p>
</section>

<section class="team" role="img" aria-label="Warm orange-tinted photo of a team working together">
  <h2 class="team-title">Our Team</h2>
  <div class="rule"></div>
  <h4>Mara Lindqvist</h4>
  <p>An experienced executive coach, senior trainer working in multicultural teams in Germany, Indonesia, Mozambique, India and underserved communities. She has been a pioneer bringing internationally recognised executive coaching thinking into new markets. Working with international organisations and international development projects in management roles for the last decade, she has developed an outstanding record in building multicultural teams and promoting cross-cultural communication and negotiation. Her research focuses on leadership and human experience in multicultural, complex, uncertain environments and the impact of new technologies in collaborative and group communication in global organisations.</p>
  <h4>Tovin Arlett</h4>
  <p>A highly experienced professional in training design and capacity development in the EU and qualified expert in migration. Tovin has five years of experience of EU affairs and policy development, and is accomplished in EU institutions and member-based organisations. Highly knowledgeable about the political environment in the EU and its stakeholders, he has developed a broad network in the public and private sector institutions. Acknowledged as a situated and committed professional with a natural aptitude for developing cross-cultural partnerships, he has managed multi-ethnic teams and is highly knowledgeable in emerging economies and multi-stakeholder partnerships and negotiation.</p>
</section>

<section class="services">
  <h2 class="section-title">Our Services</h2>
  <div class="rule"></div>
  <h2>Leadership and Organisational Development</h2>
  <p>Bright Harbour’s leadership and management development programs help managers develop themselves, develop others, improve work processes, lead organisational change, and improve team effectiveness and processes.</p>
  <p>Whilst most businesses are based on continuity by turning repetitive tasks in a more efficient and effective way, the environment that organisations face today requires permanent adaptation and change.</p>
  <p>We use our long and deep experience in organisational change and interpersonal communication to help organisations develop a coherent leadership style that ensures adaptation.</p>
  <p>We offer a new shared learning experience in:</p>
  <h5>Leader as a coach</h5>
  <p>It is designed for organisations who want to equip their line managers with the skills needed to demonstrate a more facilitative style and to get the best out of their people through a measured mix of active support and constructive challenge.</p>
  <h5>Interpersonal Communication</h5>
  <p>We offer leaders and managers the opportunity to understand the underlying mechanisms of interpersonal communication and discover their strengths and weaknesses, as well as the context of the beliefs and value systems.</p>
  <h5>Managing cross-cultural and virtual teams</h5>
  <p>There is an increasing pressure on organisations to work with highly cross-cultural and virtual teams where traditional management techniques do not always provide the expected outputs. We offer leaders and managers alternative paths for engaging their team members and improving performance.</p>
  <h5>Team Cooperation</h5>
  <p>It is designed for teams willing to understand the development of a group culture and the implications of the competition-cooperation dynamics in their performance.</p>
  <h5>Executive Coaching</h5>
  <p>Bright Harbour’s coaching programs, either face-to-face or online, help middle managers and senior leaders:</p>
  <ul>
    <li>Find practical solutions to leadership challenges, in particular for virtual and multicultural environments</li>
    <li>Identify conflicts, resources and the small actions to achieve big impact</li>
    <li>Build on the leader’s capacity to develop teams and relationships with stakeholders</li>
    <li>Improve confidence and clarify goals</li>
  </ul>
  <h5>Training</h5>
  <p>For Organisations and Projects: we enhance the effectiveness of technical and skill-based trainings through tailor-made evaluation and skills coaching for trainers.</p>
  <p>Knowledge Into Training: we help clients turn technical knowledge into high-impact training adapted to the target audience, based on adult learning practice.</p>
  <p>Training Delivery: our trainers lead 1-2 day workshops, week-long off-site programs or several-month programs linked by coaching or mentoring.</p>
  <h5>Virtual Learning</h5>
  <p>We design e-learning programs that reflect the learner’s actual work and reality so that the material is relevant and engaging. We employ various methods that capture and sustain the learner’s interest throughout an e-learning program.</p>
</section>

<section class="clients">
  <h2 class="section-title">Our Clients</h2>
  <div class="rule"></div>
  <h5>Non-profit organisations</h5>
  <p>Many NGOs have an international or global mandate supported by a slim organisational structure. The budget limitation of those organisations often limits their capacity to invest in state of the art training or leadership development in order not to hamper their advocacy, technical and project management needs.</p>
  <h5>Small and Medium Enterprises</h5>
  <p>Similar to NGOs, the commercial urgency and limited budget of small organisations often leaves training and leadership development outside the immediate strategic priorities.</p>
  <h5>Multilateral organisations &amp; Projects</h5>
  <p>Responsible for the implementation of international development or public-private projects, they rely often on external professionals to develop a team of experts and management practices in order to translate technical content in a very limited period of time.</p>
  <div class="testimonial">
    <div class="client-photo" role="img" aria-label="Portrait photo of the client in a circle"></div>
    <p class="client-role">Mr. R.T. Business Development In Emerging Markets, Spain</p>
    <p class="client-quote">“I have been impressed by Mara’s capacity to coach and train high level government officials with success. My reports show she has been able to increase their motivation in increasing their capacities of driving complex change management processes”</p>
    <svg class="next-arrow" width="44" height="90" viewBox="0 0 44 90" fill="none" stroke="#fff" stroke-width="5"><path d="M6 6 L38 45 L6 84"/></svg>
  </div>
</section>

<footer class="footer">
  <div class="map" role="img" aria-label="Street map showing the office location"></div>
  <div class="contact">
    <p class="contact-mail">info@brightharbour.be</p>
    <div class="social" aria-label="Social links"><span></span><span></span><span></span></div>
  </div>
</footer>

</body>
</html>
```